VerdantMed Business Card & Stationary
VerdantMed Pharmacy
VerdantMed Business Card & Stationary - Pharmacy/Pharmaceuticals
Creative Brief
Professional
Clara J Vandermeer RPh
Owner/Pharmacist
12 Fernleaf Way, Suite 4, Greenvale
xxx-xxx-xxxx Can use any 10 numbers for illustration purposes
clara@verdantmed-example.com
www.verdantmed-example.com
We are looking for something very stylish and creative yet professional that will capture attention and reinforce our branding strategy efforts. We would also like to have the ability with whatever digital files are sent to us to be easily changed by printing company to so that we could interchange staff members names and titles on the business cards. Please use modern symbols for phone, mobile, fax, web. No QR code needed. Would like to see the drafts using the logo color variations (silver or gold or blue and gray/silver) in the logo upload files. Thank you.
Designers Creativity. Editable Fields - need to be able to modify and list the pharmacy's services that will be offered: Willow Health Clinic Quick and Convenient Drive Thru Compounding: Traditional, Specialty, Pet Immunizations and Health Screening Delivery
belvuto belvuto
Project is Unveiled. Looking forward to your work towards refining the cards. Thank you.

```html
<!DOCTYPE html>
<html lang="en">
<head>
<meta charset="utf-8">
<title>VerdantMed Pharmacy – Stationery Set</title>
<link rel="stylesheet" href="https://fonts.googleapis.com/css2?family=Cormorant+Garamond:wght@500&family=Lato:wght@400;700&display=swap">
<style>
:root{
  --backdrop:#efe6d5;
  --teal:#7fa2a5;
  --teal-dark:#5b8488;
  --teal-light:#c9dadb;
  --gold:#b6975b;
  --gold-light:#d9c592;
  --grey:#9ea3a6;
  --grey-dark:#7f8588;
  --paper:#ffffff;
  --ink:#4c5a5c;
  --seal:#b3262a;
}
*{box-sizing:border-box;margin:0;padding:0}
html,body{width:1200px;height:214px;overflow:hidden}
body{background:var(--backdrop);font-family:"Lato",sans-serif;color:var(--ink);position:relative}
.piece{position:absolute;background:var(--paper);box-shadow:0 1px 3px rgba(0,0,0,.25);overflow:hidden}
.brand{font-family:"Cormorant Garamond",serif;font-weight:500;color:var(--teal-dark);white-space:nowrap}

/* business cards */
.card{width:104px;height:40px;padding:5px 6px}
.card .brand{font-size:10px;display:block;margin-top:6px}
.card .meta{font-size:4px;line-height:5px;margin-top:2px;white-space:nowrap}
.card .band{position:absolute;left:0;right:0;bottom:0;height:7px;background:var(--teal)}
.card.teal{background:var(--teal)}
.card.teal .brand{color:var(--paper)}
.card.teal .band{background:var(--teal-dark)}
.card.gold{background:var(--gold)}
.card.gold .brand{color:var(--paper)}
.card.gold .band{background:var(--gold-light)}
.card.grey{background:var(--grey)}
.card.grey .brand{color:var(--paper)}
.card.grey .band{background:var(--grey-dark)}
.card.goldband .band{background:var(--gold)}
.card.greyband .band{background:var(--grey)}
.card .chips{display:flex;gap:3px;margin-top:4px}
.card .chips span{width:14px;height:6px;background:var(--teal-light)}

/* letterhead */
.letterhead{left:360px;top:12px;width:132px;height:190px;padding:10px}
.letterhead .brand{font-size:12px;display:block;text-align:center}
.letterhead .body{font-size:4px;line-height:6px;margin-top:18px}
.letterhead .rule{height:2px;background:var(--teal-light);margin:3px 0}
.letterhead .foot{position:absolute;left:0;right:0;bottom:0;height:10px;background:var(--teal)}

/* disc */
.disc{left:578px;top:24px;width:68px;height:68px;border-radius:50%;background:radial-gradient(circle,var(--backdrop) 0 7px,#e6eeee 8px,var(--paper) 60%,var(--teal-light))}
.disc .brand{position:absolute;top:14px;width:100%;text-align:center;font-size:7px}

.seal{left:749px;top:22px;width:38px;height:38px;border-radius:50%;background:var(--seal)}

/* envelopes */
.envelope{left:509px;width:211px;height:54px;padding:6px 8px}
.envelope.front{top:94px}
.envelope.front .brand{font-size:8px}
.envelope.front .window{position:absolute;left:90px;top:22px;width:78px;height:18px;border:1px solid var(--teal-light)}
.envelope .stripe{position:absolute;left:0;right:0;bottom:0;height:6px;background:var(--teal)}
.envelope.back{top:150px;height:52px;padding:0}
.envelope.back svg{position:absolute;left:0;top:0}

.notepad{left:734px;top:72px;width:130px;height:130px;padding:12px 10px}
.notepad .brand{font-size:10px}
.notepad .head{position:absolute;left:0;right:0;top:0;height:6px;background:var(--teal)}
.notepad .line{height:1px;background:var(--teal-light);margin-top:11px}

.tall-envelope{left:888px;top:12px;width:96px;height:190px;background:linear-gradient(var(--paper),#f1f5f5)}
.tall-envelope svg{position:absolute;left:0;top:0}

/* folder */
.folder{left:996px;top:12px;width:197px;height:190px}
.folder .spine{position:absolute;left:0;top:0;bottom:0;width:92px;background:linear-gradient(180deg,var(--teal-light),var(--teal))}
.folder .brand{position:absolute;left:104px;top:40px;font-size:13px}
.folder .tag{position:absolute;left:104px;top:58px;font-size:5px;letter-spacing:.5px}
.folder svg{position:absolute;left:0;bottom:0}
</style>
</head>
<body>

<div class="piece card teal" style="left:12px;top:12px"><span class="brand">VerdantMed</span><div class="band"></div></div>
<div class="piece card" style="left:122px;top:12px"><span class="brand">VerdantMed</span><div class="band"></div></div>
<div class="piece card grey" style="left:232px;top:12px"><span class="brand">VerdantMed</span><div class="band"></div></div>

<div class="piece card goldband" style="left:12px;top:58px"><div class="meta">Clara J Vandermeer RPh<br>Owner/Pharmacist</div><div class="band"></div></div>
<div class="piece card gold" style="left:122px;top:58px"><span class="brand">VerdantMed</span><div class="band"></div></div>
<div class="piece card gold" style="left:232px;top:58px"><span class="brand">VerdantMed</span><div class="band"></div></div>

<div class="piece card" style="left:12px;top:104px"><div class="meta">Clara J Vandermeer RPh<br>Owner/Pharmacist<br>clara@verdantmed-example.com</div><div class="band"></div></div>
<div class="piece card greyband" style="left:122px;top:104px"><span class="brand">VerdantMed</span><div class="band"></div></div>
<div class="piece card grey" style="left:232px;top:104px"><span class="brand">VerdantMed</span><div class="band"></div></div>

<div class="piece card" style="left:12px;top:150px"><div class="meta">12 Fernleaf Way, Suite 4<br>Greenvale<br>www.verdantmed-example.com</div><div class="band"></div></div>
<div class="piece card" style="left:122px;top:150px"><div class="meta">Willow Health Clinic</div><div class="chips"><span></span><span></span><span></span><span></span></div><div class="band"></div></div>
<div class="piece card grey" style="left:232px;top:150px"><span class="brand">VerdantMed</span><div class="band"></div></div>

<div class="piece letterhead">
  <span class="brand">VerdantMed</span>
  <div class="body">Dear patient,<br>Thank you for choosing our pharmacy today.</div>
  <div class="rule"></div><div class="rule"></div><div class="rule"></div><div class="rule"></div><div class="rule"></div><div class="rule"></div>
  <div class="body" style="margin-top:8px">Clara J Vandermeer RPh</div>
  <div class="foot"></div>
</div>

<div class="piece disc"><span class="brand">VerdantMed</span></div>
<div class="piece seal" role="img" aria-label="Red wax seal"></div>

<div class="piece envelope front"><span class="brand">VerdantMed</span><div class="window"></div><div class="stripe"></div></div>
<div class="piece envelope back">
  <svg width="211" height="52" viewBox="0 0 211 52"><path d="M0 0 L105 30 L211 0" fill="none" stroke="#c9dadb" stroke-width="1.5"/></svg>
  <div class="stripe"></div>
</div>

<div class="piece notepad">
  <div class="head"></div>
  <span class="brand">VerdantMed</span>
  <div class="line"></div><div class="line"></div><div class="line"></div><div class="line"></div><div class="line"></div><div class="line"></div><div class="line"></div><div class="line"></div>
</div>

<div class="piece tall-envelope">
  <svg width="96" height="190" viewBox="0 0 96 190"><path d="M0 0 L48 60 L96 0" fill="#e4eded" stroke="#c9dadb"/><rect x="0" y="180" width="96" height="10" fill="#7fa2a5"/></svg>
</div>

<div class="piece folder">
  <div class="spine"></div>
  <span class="brand">VerdantMed</span>
  <span class="tag">PHARMACY</span>
  <svg width="197" height="80" viewBox="0 0 197 80"><path d="M92 80 L92 30 Q140 10 197 20 L197 80 Z" fill="#dfe9e9"/><path d="M0 80 L0 40 L92 30 L92 80 Z" fill="#5b8488"/></svg>
</div>

</body>
</html>
```